Web Design for an Online Dating Web Site

We need an uncoded web design for a new online dating web site called pLirvo.com. Simplicity and boldness are the key factors in the successful design.
Please look at the requirements document attached for details.
Updates
Dear all,
Please AVOID USING A PICTURE OF A HAPPY COUPLE ON THE HOME PAGE of the site. We highly want to move away from this space as it makes our web site just like another dating web site.
We like something simple with web 2.0 look and feel. The examples in the Requirements Document are exactly the design we are after.
Regards
Tarn
Industry/Entity Type
Dating
Look and feel
Each slider illustrates characteristics of the customer's brand and the style your logo design should communicate.

```html
<!DOCTYPE html>
<html lang="en">
<head>
<meta charset="utf-8">
<title>pLirvo.com – My Messages</title>
<link rel="stylesheet" href="https://fonts.googleapis.com/css2?family=Ubuntu:wght@400;500;700&family=Arimo:wght@400;700&family=Cinzel:wght@600&display=swap">
<style>
:root{
  --header-top:#ffffff;
  --header-bottom:#ececec;
  --brand-red:#c8141b;
  --brand-red-dark:#8e0c10;
  --ink:#444444;
  --btn-grey:#bdbdbd;
  --btn-grey-dark:#a3a3a3;
  --stage-light:#232323;
  --stage-dark:#040404;
  --panel:#e9e9e9;
  --panel-active:#c9c9c9;
  --rule:#d0d0d0;
  --label:#333333;
  --value:#555555;
  --muted:#7a7a7a;
  --white:#ffffff;
  --field:#1a1a1a;
  --field-text:#6a6a6a;
  --footer-band:#151515;
  --footer:#0a0a0a;
  --footer-link:#5a5a5a;
  --input:#2c2c2c;
  --photo-couple:#6e7d48;
  --photo-dark:#3b3a36;
  --avatar-pink:#d468c3;
  --avatar-blue:#4a9fd6;
}
*{margin:0;padding:0;box-sizing:border-box}
html,body{width:1200px;height:1083px;overflow:hidden}
body{position:relative;background:var(--footer);font-family:"Ubuntu",Arial,sans-serif;color:var(--white)}
.abs{position:absolute}

/* header */
.site-header{left:0;top:0;width:1200px;height:104px;background:linear-gradient(var(--header-top),var(--header-bottom));border-bottom:1px solid #cfcfcf}
.brand{left:147px;top:14px;display:flex;align-items:center;gap:12px}
.brand-dot{width:26px;height:26px;border-radius:50%;background:var(--brand-red)}
.brand-name{font-family:"Ubuntu",sans-serif;font-weight:500;font-size:58px;line-height:1;color:var(--ink);letter-spacing:-1px}
.nav-btn{top:21px;height:30px;border-radius:8px;font-size:15px;line-height:30px;text-align:center;color:var(--white);background:linear-gradient(#d3d3d3,var(--btn-grey-dark));text-shadow:0 1px 1px rgba(0,0,0,.25)}
.nav-btn.is-active{background:linear-gradient(#d81e25,var(--brand-red-dark))}
.stuff-bar{left:645px;top:60px;width:349px;height:30px;border-radius:8px;background:#1c1c1c;color:var(--white);font-size:18px;line-height:30px;text-align:center}
.stuff-bar small{font-size:10px;vertical-align:2px;margin-left:4px}

/* stage */
.stage{left:0;top:105px;width:1200px;height:678px;background:radial-gradient(ellipse 60% 70% at 50% 45%,var(--stage-light),var(--stage-dark))}
.page-title{left:177px;top:163px;font-family:"Cinzel",serif;font-weight:600;font-size:21px;letter-spacing:1.5px;color:#e6e6e6}

.inbox{left:186px;top:199px;width:311px;height:502px;border-radius:8px;background:linear-gradient(#ededed,#e2e2e2);overflow:hidden;box-shadow:0 2px 6px rgba(0,0,0,.6)}
.msg{position:absolute;left:0;width:311px;height:97px;border-bottom:1px solid var(--rule)}
.msg.is-active{background:var(--panel-active)}
.avatar{position:absolute;left:32px;top:7px;width:67px;height:67px;border:3px solid var(--white);box-shadow:0 1px 3px rgba(0,0,0,.35)}
.sender{position:absolute;left:15px;top:79px;width:100px;text-align:center;font-size:12px;color:var(--label)}
.lbl{position:absolute;width:60px;right:131px;text-align:right;font-size:12px;color:var(--label)}
.val{position:absolute;left:187px;width:118px;font-size:12.5px;color:var(--value);white-space:nowrap;overflow:hidden;padding-left:4px;border-left:1px solid var(--rule)}
.val.first{border-bottom:1px solid var(--rule);padding-bottom:3px}
.date{position:absolute;left:113px;font-size:10px;letter-spacing:.5px;color:#8a8a8a}

.pager-tab{top:322px;width:70px;height:69px;background:linear-gradient(#f4f4f4,#cfcfcf);box-shadow:0 3px 4px rgba(0,0,0,.5)}
.pager-tab.prev{left:0;border-radius:0 6px 6px 0}
.pager-tab.next{left:1130px;border-radius:6px 0 0 6px}
.pager-tab svg{position:absolute;left:17px;top:14px}

.reader-photo{left:559px;top:256px;width:147px;height:134px;border:3px solid var(--white);background:linear-gradient(135deg,var(--photo-couple),#4d5a2f 55%,#8c2a56)}
.reader-name{left:714px;top:298px;font-size:19px}
.reader-date{left:714px;top:321px;font-size:10px;color:var(--muted);letter-spacing:.5px}
.field-title{left:560px;font-size:18px}
.field{background:var(--field);color:var(--field-text);font-size:12.5px;line-height:15px;padding:4px 6px}

.dots{left:548px;top:739px;display:flex;gap:18px}
.dots span{width:12px;height:12px;border-radius:50%;background:#111;box-shadow:inset 0 1px 2px #000}
.dots span.is-current{background:var(--brand-red)}

/* footer */
.footer-band{left:0;top:783px;width:1200px;height:25px;background:var(--footer-band)}
.foot-head{top:786px;font-family:"Arimo",sans-serif;font-size:13px;color:var(--white)}
.foot-links{left:247px;top:816px;list-style:none;font-family:"Arimo",sans-serif;font-size:11px;line-height:16px;color:var(--footer-link)}
.input{left:419px;width:124px;height:23px;border-radius:3px;background:var(--input);font-family:"Arimo",sans-serif;font-size:10px;color:#666;padding:5px 10px}
.send{left:419px;top:999px;width:67px;height:22px;border-radius:3px;background:#2a2a2a;font-size:13px;line-height:22px;text-align:center}
.social{top:819px;width:23px;height:23px;border-radius:4px}
.plus-box{left:650px;top:850px;width:38px;height:24px;border-radius:3px;background:#eaeaea}
.count{left:693px;top:850px;width:40px;height:24px;border-radius:3px;background:#fafafa;color:#333;font-size:12px;line-height:24px;text-align:center}
.like-box{left:650px;top:882px;width:48px;height:24px;border-radius:3px;background:#eef1f7;border:1px solid #c5ccdb}
.like-sq{left:705px;top:888px;width:11px;height:11px;background:#5a6fa3}
.like-txt{left:721px;top:887px;font-family:"Arimo",sans-serif;font-size:11px;color:var(--footer-link)}
.contact{left:847px;top:816px;font-family:"Arimo",sans-serif;font-size:10.5px;line-height:16px;color:var(--footer-link)}
.contact .phone{color:#bbb}
.foot-brand{left:849px;top:868px;display:flex;align-items:center;gap:8px}
.foot-brand .brand-name{font-size:34px;color:#7d7d7d}
.foot-brand .brand-dot{width:14px;height:14px;background:#7d7d7d}
.legal{left:0;top:1049px;width:1200px;text-align:center;font-family:"Arimo",sans-serif;font-size:10px;line-height:14px;color:#5e5e5e}
</style>
</head>
<body>

<header class="site-header abs">
  <div class="brand abs"><span class="brand-name">plirvo</span><span class="brand-dot"></span></div>
  <nav>
    <div class="nav-btn abs is-active" style="left:620px;width:122px">my messages</div>
    <div class="nav-btn abs" style="left:751px;width:103px">start dating</div>
    <div class="nav-btn abs" style="left:862px;width:86px">sign out</div>
    <div class="nav-btn abs" style="left:956px;width:62px">help</div>
    <div class="stuff-bar abs">my stuff<small>▼</small></div>
  </nav>
</header>

<main class="stage abs"></main>
<h1 class="page-title abs">MY MESSAGES</h1>

<section class="inbox abs">
  <div class="msg is-active" style="top:11px">
    <div class="avatar" role="img" aria-label="Profile photo of a couple outdoors" style="background:linear-gradient(135deg,var(--photo-couple),#8c2a56)"></div>
    <div class="sender">Lena</div>
    <div class="lbl" style="top:17px">Subject:</div><div class="val first" style="top:16px">Whats up cut...</div>
    <div class="lbl" style="top:40px">Message:</div><div class="val" style="top:39px">You should te...</div>
    <div class="date" style="top:63px">10/05/2011</div>
  </div>
  <div class="msg" style="top:109px">
    <div class="avatar" role="img" aria-label="Profile photo of two friends" style="background:linear-gradient(135deg,var(--photo-dark),#8a6a55)"></div>
    <div class="sender" style="top:75px">Brielle</div>
    <div class="lbl" style="top:17px">Subject:</div><div class="val first" style="top:16px">I'm new here...</div>
    <div class="lbl" style="top:40px">Message:</div><div class="val" style="top:39px">I want to set...</div>
    <div class="date" style="top:63px">10/03/2011</div>
  </div>
  <div class="msg" style="top:207px">
    <div class="avatar" role="img" aria-label="Default female profile placeholder" style="background:linear-gradient(#f4f4f4,#dcdcdc 55%,var(--avatar-pink))"></div>
    <div class="sender" style="top:76px">Marisa</div>
    <div class="lbl" style="top:17px">Subject:</div><div class="val first" style="top:16px">I'm new here...</div>
    <div class="lbl" style="top:40px">Message:</div><div class="val" style="top:39px">I want to set...</div>
    <div class="date" style="top:62px">09/27/2011</div>
  </div>
  <div class="msg" style="top:304px">
    <div class="avatar" role="img" aria-label="Default male profile placeholder" style="background:linear-gradient(#f4f4f4,#dcdcdc 55%,var(--avatar-blue))"></div>
    <div class="sender" style="top:75px">Corbin</div>
    <div class="lbl" style="top:17px">Subject:</div><div class="val first" style="top:16px">I'm new here...</div>
    <div class="lbl" style="top:40px">Message:</div><div class="val" style="top:39px">I want to set...</div>
    <div class="date" style="top:62px">09/23/2011</div>
  </div>
  <div class="msg" style="top:401px;border-bottom:0">
    <div class="avatar" role="img" aria-label="Profile photo of a couple outdoors" style="background:linear-gradient(135deg,var(--photo-couple),#8c2a56)"></div>
    <div class="sender" style="top:76px">Lena</div>
    <div class="lbl" style="top:17px">Subject:</div><div class="val first" style="top:16px">I'm new here...</div>
    <div class="lbl" style="top:40px">Message:</div><div class="val" style="top:39px">I want to set...</div>
    <div class="date" style="top:62px">09/15/2011</div>
  </div>
</section>

<div class="pager-tab prev abs"><svg width="36" height="40" viewBox="0 0 36 40"><path d="M30 2 L8 20 L30 38" fill="none" stroke="#222" stroke-width="9" stroke-linejoin="miter"/></svg></div>
<div class="pager-tab next abs"><svg width="36" height="40" viewBox="0 0 36 40" style="left:21px"><path d="M6 2 L28 20 L6 38" fill="none" stroke="#222" stroke-width="9" stroke-linejoin="miter"/></svg></div>

<article>
  <div class="reader-photo abs" role="img" aria-label="Profile photo of a couple in a green park"></div>
  <div class="reader-name abs">Lena Marsh</div>
  <div class="reader-date abs">10/05/2011</div>
  <div class="field-title abs" style="top:407px">Subject</div>
  <div class="field abs" style="left:555px;top:435px;width:173px">Whats up cutie? Let's Talk</div>
  <div class="field-title abs" style="top:472px">Message</div>
  <div class="field abs" style="left:554px;top:496px;width:499px;height:85px">You should text me sometime ;) 555.014.2870<br>sample text, sample text, sample text, sample text, sample text,<br>sample text, sample text, sample text, sample text, sample text, sample text,<br>sample text, sample text, sample text, sample text,<br>sample text, sample text, sample text, sample text, sample text,</div>
</article>

<div class="dots abs"><span class="is-current"></span><span></span><span></span><span></span><span></span></div>

<footer>
  <div class="footer-band abs"></div>
  <div class="foot-head abs" style="left:248px">Read More</div>
  <div class="foot-head abs" style="left:422px">Let's Talk</div>
  <div class="foot-head abs" style="left:651px">Get Social</div>
  <div class="foot-head abs" style="left:848px">Contact Us</div>

  <ul class="foot-links abs">
    <li>Why pLirvo?</li><li>How It Works</li><li>Sign Up</li><li>Login</li><li>About Us</li>
  </ul>

  <div class="input abs" style="top:819px">name</div>
  <div class="input abs" style="top:849px">email address</div>
  <div class="input abs" style="top:879px;width:181px;height:114px">type message here...</div>
  <div class="send abs">Send</div>

  <div class="social abs" style="left:650px;background:#3b5c9a"></div>
  <div class="social abs" style="left:680px;background:#e58a1e"></div>
  <div class="social abs" style="left:710px;background:#3d9bd3"></div>
  <div class="social abs" style="left:740px;background:#1f8a5a"></div>
  <div class="plus-box abs"></div>
  <div class="count abs">1.4k</div>
  <div class="like-box abs"></div>
  <div class="like-sq abs"></div>
  <div class="like-txt abs">3,400 Likes</div>

  <div class="contact abs">118 Sample Lane<br>40012, Kestrel<br><span class="phone">1.800.555.0199</span></div>
  <div class="foot-brand abs"><span class="brand-name">plirvo</span><span class="brand-dot"></span></div>

  <p class="legal abs">© 2011 pLirvo.com<br>pLirvo #1 Trusted Relationship Site - Know Your Match</p>
</footer>

</body>
</html>
```